Need Flyer for Our Real estate Agency

Need to run General Campaign for our agency with Start of New Year as our theme ..Must have an agent's picture on the DL..
Address:
9 / 386Barwin rd, Truganina VIC 3029
Ph:03 9142 7305
email:info@koridanrealestate.example.au
www.koridanrealestate.example.au
Something like as attached picture..
Target Market(s)
Home Buyers
Industry/Entity Type
Real Estate Agent
Requirements
Must have
- Our Logo Colours

```html
<!DOCTYPE html>
<html lang="en">
<head>
<meta charset="utf-8">
<title>Koridan Real Estate – DL Flyer</title>
<link rel="stylesheet" href="https://fonts.googleapis.com/css2?family=Raleway:wght@600;700&family=Fira+Sans:wght@300;400&display=swap">
<style>
  :root {
    --page-bg: #ffffff;
    --flyer-black: #0c0b0b;
    --flyer-glow: #231f20;
    --ink-white: #ffffff;
    --accent-yellow: #f7ec13;
    --gold: #c9a43a;
    --gold-light: #f1d88a;
    --sky: #d8e3ea;
    --building: #b9c3c9;
    --suit: #2a2b2b;
  }
  * { margin: 0; padding: 0; box-sizing: border-box; }
  html, body {
    width: 1200px; height: 1200px; overflow: hidden;
    background: var(--page-bg);
  }
  .flyer {
    position: absolute; left: 58px; top: 345px;
    width: 1085px; height: 510px;
    background: radial-gradient(ellipse at 40% 45%, var(--flyer-glow) 0%, var(--flyer-black) 70%);
    overflow: hidden;
  }
  .glitter {
    position: absolute; left: 500px; top: 0; width: 585px; height: 510px;
    background:
      radial-gradient(ellipse at 40% 10%, rgba(201,164,58,0.28) 0%, rgba(201,164,58,0) 45%),
      radial-gradient(ellipse at 75% 95%, rgba(201,164,58,0.3) 0%, rgba(201,164,58,0) 45%),
      radial-gradient(ellipse at 98% 50%, rgba(201,164,58,0.22) 0%, rgba(201,164,58,0) 30%);
  }
  .brand {
    position: absolute; left: 55px; top: 92px; width: 178px;
    font-family: "Raleway", sans-serif; font-weight: 600;
    font-size: 31px; letter-spacing: 3px; color: var(--ink-white);
    text-align: center;
  }
  .headline {
    position: absolute; left: 55px; top: 186px;
    font-family: "Raleway", sans-serif; font-weight: 700;
    font-size: 38px; line-height: 46px; color: var(--ink-white);
  }
  .headline .highlight { color: var(--accent-yellow); }
  .intro {
    position: absolute; left: 55px; top: 292px; width: 407px;
    border-top: 2px solid var(--ink-white);
    border-bottom: 2px solid var(--ink-white);
    padding: 9px 0 12px;
    font-family: "Fira Sans", sans-serif; font-weight: 300;
    font-size: 24px; line-height: 30px; color: var(--ink-white);
  }
  .contact {
    position: absolute; left: 55px; top: 408px;
    font-family: "Fira Sans", sans-serif; font-weight: 300;
    font-size: 16px; line-height: 23.5px; color: var(--ink-white);
  }
  .contact .divider { margin: 0 8px; }
  .agent-photo {
    position: absolute; left: 645px; top: 62px; width: 387px; height: 386px;
    border: 3px solid var(--gold);
    box-shadow: 0 0 0 1px var(--gold-light) inset;
    background:
      linear-gradient(180deg, var(--sky) 0%, #e9eef1 35%, var(--building) 62%, var(--suit) 100%);
  }
</style>
</head>
<body>
  <section class="flyer">
    <div class="glitter" role="img" aria-label="Scattered gold glitter sparkles"></div>

    <div class="brand">KORIDAN</div>

    <h1 class="headline">Curious to Know <span class="highlight">What</span><br><span class="highlight">Your Home is Worth?</span></h1>

    <p class="intro">Is simply dummy text of the printing and typesetting industry. Lorem.</p>

    <div class="contact">
      <p>Phone: 03 9142 7305<span class="divider">|</span>Email: info@koridanrealestate.example.au</p>
      <p>Web: www.koridanrealestate.example.au</p>
      <p>Address: 9 / 386Barwin rd, Truganina VIC 3029</p>
    </div>

    <div class="agent-photo" role="img" aria-label="Photo of a smiling real estate agent in a dark suit holding a tablet, with a waterfront apartment building behind him"></div>
  </section>
</body>
</html>
```